Business Card Design Project for Investment Fund

Veloria Capital Management is an emerging wealth management firm based in New Jersey. It offers superior investment returns to high net worth individuals and institutions by finding undervalued assets.
We recently selected a company logo which was inspired by the Tucana constellation. Beta Tucanae is a group of six stars, containing star cluster 47 Tucanae, rated the second brightest object in the sky.
Now we need a business card design. Since we are an investment firm, the design should project a sense of stability, growth and professionalism. The owner is interested in something simple yet striking, which of course is consistent with the logo.
Wealthy individuals, probably middle aged or older, in the US
Investment

```html
<!DOCTYPE html>
<html lang="en">
<head>
<meta charset="utf-8">
<title>Veloria Capital Management – Business Card</title>
<link href="https://fonts.googleapis.com/css2?family=Open+Sans:wght@400;600;700&display=swap" rel="stylesheet">
<style>
  :root {
    --stage: #2a2a2c;
    --navy: #1c2238;
    --navy-deep: #141a2c;
    --paper: #f4f4f5;
    --paper-shade: #e2e2e4;
    --ink: #4a4a4e;
    --ink-soft: #6b6b70;
    --mark: #3a3fa8;
    --rule: #a9a9ad;
  }
  * { margin: 0; padding: 0; box-sizing: border-box; }
  html, body { width: 1200px; height: 900px; overflow: hidden; }
  body {
    background: var(--stage);
    font-family: "Open Sans", sans-serif;
    display: flex;
    flex-direction: column;
    align-items: center;
    justify-content: center;
    gap: 60px;
  }
  .card {
    width: 630px;
    height: 360px;
    background: var(--navy);
    display: flex;
    flex-direction: column;
    justify-content: center;
    box-shadow: 0 8px 24px rgba(0,0,0,.45);
  }
  .card__band {
    height: 200px;
    background: linear-gradient(180deg, var(--paper) 0%, #ffffff 45%, var(--paper-shade) 100%);
    display: flex;
    align-items: center;
  }
  .card--front .card__band { justify-content: center; }
  .brand {
    display: flex;
    flex-direction: column;
    align-items: center;
    gap: 10px;
  }
  .brand__square {
    width: 64px;
    height: 64px;
    border-radius: 10px;
    background: var(--mark);
  }
  .brand__name {
    color: var(--ink);
    font-weight: 600;
    font-size: 17px;
    text-align: center;
    line-height: 1.25;
  }
  .card--back .card__band { padding: 0 40px 0 50px; }
  .card--back .brand { width: 230px; }
  .card__divider {
    width: 1px;
    height: 150px;
    background: var(--rule);
    margin: 0 30px 0 20px;
  }
  .contact { color: var(--ink); }
  .contact__name { font-weight: 700; font-size: 17px; line-height: 1.1; }
  .contact__title { font-weight: 700; font-size: 13px; margin-bottom: 12px; }
  .contact__line { font-size: 12.5px; color: var(--ink-soft); line-height: 1.35; }
  .contact__gap { height: 12px; }
</style>
</head>
<body>
  <section class="card card--front" aria-label="Card front">
    <div class="card__band">
      <div class="brand">
        <div class="brand__square"></div>
        <div class="brand__name">Veloria<br>Capital Management</div>
      </div>
    </div>
  </section>

  <section class="card card--back" aria-label="Card back">
    <div class="card__band">
      <div class="brand">
        <div class="brand__square"></div>
        <div class="brand__name">Veloria<br>Capital Management</div>
      </div>
      <div class="card__divider"></div>
      <div class="contact">
        <p class="contact__name">Daniel Ross</p>
        <p class="contact__title">CEO</p>
        <p class="contact__line">48 Harbor Ave.</p>
        <p class="contact__line">Newark, NJ 07102</p>
        <div class="contact__gap"></div>
        <p class="contact__line">dross@veloriacapmgmt.com</p>
        <p class="contact__line">ph: 201-555-0142</p>
        <div class="contact__gap"></div>
        <p class="contact__line">www.veloriacapmgmt.com</p>
      </div>
    </div>
  </section>
</body>
</html>
```